Varrowick Biomedical Research Institute (VBRI) Web Design

VBRI is a non-profit organization focused on saving the lives of terminally ill patients by becoming the leaders in cutting-edge research, innovative technologies, utilizing national and international partnerships as well as the associated allopathic and naturopathic treatments necessary to do so.

Our primary focus is raising funds to support the research and acquisition of new technologies for life saving treatments which are NOT a one size fits all approach like conventional medicine but rather a marriage of the latest technologies used in combination with other new treatment possibilities for a successful end result.

Our domain is varrowickbr.org

Logo files are attached.

Looking for something clean, light, healthy.

Target Market(s)

The site should look and feel towards research/scientific grant writing.
Medical professionals, Medical Scientists.

Industry/Entity Type

Medical And Science

Number of Pages Required

4 page

Requirements
Nice to have
• Here are examples of sites I like in the order of how much I like them.
• https://www.palvenhope.org/give.html
• https://www.thekqtf.org/donate-to-kqtf
• https://www.curewaveinst.org/we-are-cwi/join-the-cause
• https://www.healquest.org/involved/donate.html
• https://give.nptf.org/checkout/donation?eid=58217
• https://www.moravind.org/how-you-can-help
• https://donate3.healquest.org/

```html
<!DOCTYPE html>
<html lang="en">
<head>
<meta charset="utf-8">
<title>Varrowick Biomedical Research Institute</title>
<link href="https://fonts.googleapis.com/css2?family=Roboto:wght@400;500;700&family=Open+Sans:wght@400;600&display=swap" rel="stylesheet">
<style>
:root{
  --green:#3f9a3a;
  --green-dark:#2f7f2c;
  --blue:#1b7fd3;
  --blue-deep:#0f5fae;
  --ink:#2b2b2b;
  --muted:#6d6d6d;
  --footer:#1f1f1f;
  --footer-bar:#161616;
  --white:#ffffff;
}
*{margin:0;padding:0;box-sizing:border-box}
html,body{width:1200px;height:3422px;overflow:hidden;background:var(--white)}
body{position:relative;font-family:"Open Sans",Arial,sans-serif;color:var(--ink)}
.abs{position:absolute}
h1,h2,h3,.nav a,.btn,.brand-name{font-family:"Roboto",Arial,sans-serif}

/* header */
.site-header{left:0;top:0;width:1200px;height:114px;background:var(--white)}
.brand{display:flex;align-items:center;gap:14px}
.brand-mark{width:52px;height:52px;border-radius:50%;background:var(--green)}
.brand-name{font-size:44px;font-weight:700;color:var(--blue);letter-spacing:1px}
.phone{left:760px;top:24px;font-size:21px;color:#444;display:flex;align-items:center;gap:10px}
.btn-donate{left:958px;top:20px;width:140px;height:39px;background:var(--green);color:#fff;font-size:15px;font-weight:700;display:flex;align-items:center;justify-content:center;border-radius:2px}
.nav{left:474px;top:80px}
.nav a{position:absolute;white-space:nowrap;font-size:15px;font-weight:500;color:#333;text-decoration:none;top:0}
.nav a.active{color:var(--green)}

/* hero */
.hero{left:0;top:114px;width:1200px;height:570px;background:radial-gradient(ellipse at 50% 35%,#5f8fa6 0%,#2d5f7a 35%,#113850 70%,#0a2234 100%)}
.hero-title{left:0;top:404px;width:1200px;text-align:center;color:#fff}
.hero-title h1{font-size:46px;font-weight:700;line-height:54px;letter-spacing:.5px}
.hero-title .sub{display:block;font-size:38px;line-height:44px}
.dots{left:568px;top:525px;display:flex;gap:10px}
.dots span{width:11px;height:11px;border-radius:50%;background:rgba(255,255,255,.75)}
.dots span.on{background:#fff;box-shadow:0 0 0 2px rgba(255,255,255,.4)}
.hero-curve{left:0;top:614px}

/* welcome */
.welcome-media{left:98px;top:760px;width:440px;height:285px;background:linear-gradient(135deg,#8a9aa8,#4b5d70 55%,#2f3d4c);border:6px solid #eee}
.play{left:290px;top:880px;width:48px;height:48px;border-radius:50%;background:#fff;border:3px solid #222}
.play::after{content:"";position:absolute;left:16px;top:11px;border-left:15px solid #222;border-top:10px solid transparent;border-bottom:10px solid transparent}
.welcome-title{left:593px;top:762px;font-size:38px;font-weight:400;color:#333}
.welcome-title em{font-style:normal;color:var(--green)}
.welcome-text{left:593px;top:826px;width:515px;font-size:12px;line-height:23px;color:#555}
.welcome-text p{margin-bottom:12px}
.btn-solid{background:var(--green);color:#fff;font-size:13px;display:flex;align-items:center;justify-content:center;border-radius:2px}
.welcome-btn{margin-top:18px;width:106px;height:32px}

/* services */
.services{left:0;top:1145px;width:1200px;height:515px;background:linear-gradient(180deg,#1e86d8,#1572c6)}
.services-art{left:300px;top:1145px;width:600px;height:515px;background:radial-gradient(ellipse at 50% 40%,rgba(255,255,255,.14),rgba(255,255,255,0) 65%)}
.section-title-light{left:0;top:1218px;width:1200px;text-align:center;color:#fff;font-size:34px;font-weight:500}
.service{width:330px;text-align:center;color:#fff}
.service .icon{width:106px;height:106px;border-radius:50%;background:#fff;margin:0 auto;display:flex;align-items:center;justify-content:center}
.service h3{margin-top:30px;font-size:15px;font-weight:500}
.service p{margin:12px auto 0;width:300px;font-size:12px;line-height:21px}
.btn-outline-light{display:inline-block;margin-top:16px;border:1px solid rgba(255,255,255,.85);color:#fff;font-size:11px;padding:6px 10px;font-family:"Roboto",Arial,sans-serif}

/* research */
.section-title{left:0;top:1730px;width:1200px;text-align:center;font-size:32px;font-weight:500;color:#333}
.card{width:312px}
.card .media{height:178px}
.card h3{margin-top:22px;font-family:"Open Sans",Arial,sans-serif;font-size:15px;font-weight:400;color:#333}
.card p{margin-top:8px;font-size:11.5px;line-height:21px;color:#777}
.btn-outline{display:inline-block;margin-top:14px;border:1px solid #888;color:#444;font-size:11px;padding:5px 9px;font-family:"Roboto",Arial,sans-serif}

/* donor */
.donor{left:0;top:2215px;width:1200px;height:420px;background:linear-gradient(180deg,#4c9c43,#3c8f36)}
.donor-title{left:0;top:2328px;width:1200px;text-align:center;color:#fff;font-size:34px;font-weight:700}
.donor-text{left:210px;top:2392px;width:780px;text-align:center;color:#fff;font-size:12.5px;line-height:20px}
.donor-btn{left:477px;top:2475px;width:246px;height:37px;border:1px solid #fff;color:#fff;font-size:14px;display:flex;align-items:center;justify-content:center;font-family:"Roboto",Arial,sans-serif}

/* blog */
.blog-title{left:98px;top:2690px;font-size:31px;font-weight:500;color:#222}
.blog-arrows{left:1074px;top:2698px;font-size:22px;color:#444;letter-spacing:10px}
.post{display:flex;gap:27px}
.post .media{width:187px;height:164px;flex:none}
.post h3{font-family:"Open Sans",Arial,sans-serif;font-size:15px;font-weight:400;color:#444}
.post .date{margin-top:16px;font-size:11.5px;color:var(--blue);font-weight:600}
.post p{margin-top:10px;width:255px;font-size:11px;line-height:18px;color:#777}
.post .more{margin-top:12px;font-size:12px;color:#444}

/* footer */
.footer-curve{left:0;top:2975px}
.footer{left:0;top:3040px;width:1200px;height:302px;background:var(--footer);color:#ddd}
.footer-bar{left:0;top:3342px;width:1200px;height:80px;background:var(--footer-bar);color:#ccc;font-size:12px;display:flex;align-items:center;justify-content:center}
.footer-brand{left:103px;top:3140px}
.footer-brand .brand-mark{width:48px;height:48px}
.footer-brand .brand-name{font-size:40px;color:#4da0e6}
.socials{left:103px;top:3228px;display:flex;gap:7px}
.socials span{width:24px;height:24px;border-radius:50%;border:1.5px solid #ddd}
.footer-col h3{font-size:18px;font-weight:500;color:#fff;letter-spacing:.3px}
.news{left:383px;top:3108px;width:240px}
.news p{margin-top:14px;font-size:11.5px;line-height:18px;color:#ccc}
.news .field{margin-top:16px;width:228px;height:41px;background:#fff;color:#777;font-size:11px;display:flex;align-items:center;padding-left:12px}
.news .btn-solid{margin-top:16px;width:103px;height:41px;font-size:12px}
.contact{left:680px;top:3108px;width:260px;font-size:12px;color:#ddd}
.contact .addr{margin-top:18px;line-height:20px}
.contact .row{display:flex;align-items:center;gap:16px;margin-top:16px}
.links{left:992px;top:3108px;font-size:12px;color:#ddd}
.links ul{list-style:none;margin-top:16px}
.links li{height:22.4px;display:flex;align-items:center;gap:10px}
.links li::before{content:"";border-left:6px solid #ddd;border-top:4px solid transparent;border-bottom:4px solid transparent}
</style>
</head>
<body>

<header class="site-header abs">
  <div class="brand abs" style="left:103px;top:18px"><span class="brand-mark"></span><span class="brand-name">VBRI</span></div>
  <div class="phone abs">
    <svg width="18" height="18" viewBox="0 0 24 24"><path fill="#3f9a3a" d="M6.6 10.8a15.1 15.1 0 0 0 6.6 6.6l2.2-2.2c.3-.3.7-.4 1-.2 1.1.4 2.3.6 3.6.6.6 0 1 .4 1 1V20c0 .6-.4 1-1 1A17 17 0 0 1 3 4c0-.6.4-1 1-1h3.5c.6 0 1 .4 1 1 0 1.3.2 2.5.6 3.6.1.3 0 .7-.2 1z"/></svg>
    (08) 5550 1470
  </div>
  <div class="btn-donate abs">DONATE NOW +</div>
  <nav class="nav abs">
    <a class="active" style="left:0">HOME</a>
    <a style="left:73px">ABOUT US</a>
    <a style="left:176px">SERVICES</a>
    <a style="left:270px">OUR VISION</a>
    <a style="left:379px">DONATE</a>
    <a style="left:466px">BLOG</a>
    <a style="left:534px">CONTACT US</a>
  </nav>
</header>

<section class="hero abs" role="img" aria-label="Glowing wireframe human figure over a blue digital grid"></section>
<div class="hero-title abs"><h1>VARROWICK BIOMEDICAL<span class="sub">RESEARCH INSTITUTE</span></h1></div>
<div class="dots abs"><span class="on"></span><span></span><span></span><span></span></div>
<svg class="hero-curve abs" width="1200" height="72" viewBox="0 0 1200 72">
  <path d="M0 72 L0 58 C300 20 700 50 1200 0 L1200 72 Z" fill="#fff"/>
  <path d="M0 56 C300 18 700 48 1200 -2" fill="none" stroke="#3f9a3a" stroke-width="6"/>
  <path d="M0 64 C320 30 720 54 1200 10" fill="none" stroke="#1b7fd3" stroke-width="2.5"/>
</svg>

<div class="welcome-media abs" role="img" aria-label="Researcher working at lab computer monitors"></div>
<div class="play abs"></div>
<h2 class="welcome-title abs">WELCOME TO <em>VBRI</em></h2>
<div class="welcome-text abs">
  <p>Lorem ipsum dolor sit amet, consectetur adipiscing elit, sed do eiusmod tempor incididunt ut labore et dolore magna aliqua. Ut enim ad minim veniam, quis nostrud exercitation ullamco laboris nisi ut aliquip ex ea commodo consequat. Duis aute irure dolor in reprehenderit in voluptate velit esse cillum dolore eu fugiat nulla pariatur.</p>
  <p>Quisque porttitor faucibus aliquet. Sed sit amet condimentum arcu, ac placerat arcu. Nulla efficitur tincidunt orci eu semper. Aliquam gravida, velit id maximus</p>
  <div class="btn-solid welcome-btn">READ MORE</div>
</div>

<section class="services abs"></section>
<div class="services-art abs" role="img" aria-label="Faint wireframe human figure"></div>
<h2 class="section-title-light abs">OUR SERVICES</h2>

<div class="service abs" style="left:90px;top:1316px">
  <div class="icon"><svg width="48" height="48" viewBox="0 0 48 48" fill="none" stroke="#1b7fd3" stroke-width="2.5"><rect x="10" y="11" width="28" height="19" rx="1"/><path d="M5 35h38l-3 3H8z"/></svg></div>
  <h3>INNOVATIVE TECHNOLOGIES</h3>
  <p>Lorem ipsum dolor sit amet, consectetur adipiscing elit, sed do eiusmod tempor incididunt ut labore et dolore magna aliqua. Ut enim ad minim</p>
  <span class="btn-outline-light">READ MORE ●</span>
</div>
<div class="service abs" style="left:435px;top:1316px">
  <div class="icon"><svg width="48" height="48" viewBox="0 0 48 48"><path d="M19 8h10v11h11v10H29v11H19V29H8V19h11z" fill="#1b7fd3"/></svg></div>
  <h3>ASSOCIATED ALLOPATHIC</h3>
  <p>Lorem ipsum dolor sit amet, consectetur adipiscing elit, sed do eiusmod tempor incididunt ut labore et dolore magna aliqua. Ut enim ad minim</p>
  <span class="btn-outline-light">READ MORE ●</span>
</div>
<div class="service abs" style="left:770px;top:1316px">
  <div class="icon"><svg width="50" height="50" viewBox="0 0 50 50" fill="none" stroke="#1b7fd3" stroke-width="2.2"><circle cx="25" cy="25" r="19"/><path d="M25 12c8 6 8 16 0 24-8-8-8-18 0-24zM25 18v22"/></svg></div>
  <h3>NATUROPATHIC TREATMENTS</h3>
  <p>Lorem ipsum dolor sit amet, consectetur adipiscing elit, sed do eiusmod tempor incididunt ut labore et dolore magna aliqua. Ut enim ad minim</p>
  <span class="btn-outline-light">READ MORE ●</span>
</div>

<h2 class="section-title abs">VARROWICK BIOMEDICAL RESEARCH INSTITUTE</h2>
<article class="card abs" style="left:98px;top:1825px">
  <div class="media" role="img" aria-label="Scientist in lab coat with test tubes" style="background:linear-gradient(135deg,#dfe8ef,#9fb6c8 60%,#6f8ca3)"></div>
  <h3>Sed ut perspiciatis unde omnis iste</h3>
  <p>Sed ut perspiciatis unde omnis iste natus error sit voluptatem accusantium doloremque laudantium, totam</p>
  <span class="btn-outline">READ MORE ●</span>
</article>
<article class="card abs" style="left:443px;top:1825px">
  <div class="media" role="img" aria-label="Research exhibition with monitors and equipment" style="background:linear-gradient(135deg,#c9d2dc,#7d8fa2 55%,#3e4d5f)"></div>
  <h3>Sed ut perspiciatis unde omnis iste</h3>
  <p>Sed ut perspiciatis unde omnis iste natus error sit voluptatem accusantium doloremque laudantium, totam</p>
  <span class="btn-outline">READ MORE ●</span>
</article>
<article class="card abs" style="left:789px;top:1825px">
  <div class="media" role="img" aria-label="Green abstract DNA strand" style="background:radial-gradient(circle at 40% 40%,#b6e04a,#6aa71f 55%,#2f5e0f)"></div>
  <h3>Sed ut perspiciatis unde omnis iste</h3>
  <p>Sed ut perspiciatis unde omnis iste natus error sit voluptatem accusantium doloremque laudantium, totam</p>
  <span class="btn-outline">READ MORE ●</span>
</article>

<section class="donor abs" role="img" aria-label="Group of smiling supporters behind a green overlay"></section>
<h2 class="donor-title abs">BECOME A MONTHLY DONOR</h2>
<p class="donor-text abs">Sed ut perspiciatis unde omnis iste natus error sit voluptatem accusantium doloremque laudantium, totam rem aperiam, eaque ipsa quae ab illo inventore veritatis et quasi architecto beatae vitae dicta sunt explicabo. Nemo enim ipsam voluptatem quia voluptas sit aspernatur aut odit aut fugit, sed quia consequuntur magni dolores eos qui ratione voluptatem sequi nesciunt</p>
<div class="donor-btn abs">BECOME A MONTHLY DONOR</div>

<h2 class="blog-title abs">LATEST BLOG</h2>
<div class="blog-arrows abs">‹ ›</div>
<article class="post abs" style="left:98px;top:2767px">
  <div class="media" role="img" aria-label="Hands stacked together in a team huddle" style="background:linear-gradient(135deg,#9bbf6a,#c79a6c 55%,#7f6a52)"></div>
  <div>
    <h3>Nulla at diam ornare, aliquam urna</h3>
    <div class="date">APRIL 25, 2017</div>
    <p>Nulla at diam ornare, aliquam urna vel, commodo urna. Nam id risus a est luctus consectetur quis eget libero. Suspendisse potenti. Pellentesque habitant morbi tristique senectus.</p>
    <div class="more">Read More +</div>
  </div>
</article>
<article class="post abs" style="left:630px;top:2767px">
  <div class="media" role="img" aria-label="Older couple walking outdoors" style="background:linear-gradient(135deg,#c8cfc4,#8e9a86 55%,#5b6655)"></div>
  <div>
    <h3>Nulla at diam ornare, aliquam urna</h3>
    <div class="date">APRIL 25, 2017</div>
    <p>Nulla at diam ornare, aliquam urna vel, commodo urna. Nam id risus a est luctus consectetur quis eget libero. Suspendisse potenti. Pellentesque habitant morbi tristique senectus.</p>
    <div class="more">Read More +</div>
  </div>
</article>

<svg class="footer-curve abs" width="1200" height="70" viewBox="0 0 1200 70">
  <path d="M0 70 L0 48 C400 80 800 10 1200 20 L1200 70 Z" fill="#1f1f1f"/>
  <path d="M0 44 C400 76 800 6 1200 16" fill="none" stroke="#1b7fd3" stroke-width="5"/>
  <path d="M300 40 C600 30 850 0 1200 4" fill="none" stroke="#3f9a3a" stroke-width="6"/>
</svg>
<footer class="footer abs"></footer>
<div class="footer-brand brand abs"><span class="brand-mark"></span><span class="brand-name">VBRI</span></div>
<div class="socials abs"><span></span><span></span><span></span><span></span></div>

<div class="news footer-col abs">
  <h3>NEWSLETTER SIGNUP</h3>
  <p>Excepteur sint occaecat cupidatat non proident, sunt in culpa qui</p>
  <div class="field">Enter email</div>
  <div class="btn-solid">SUBSCRIBE</div>
</div>

<div class="contact footer-col abs">
  <h3>CONTACT US</h3>
  <div class="addr">Varrowick Biomedical Research Institute<br>No 2218 Larkfield Rd. Brennet, MO 60419</div>
  <div class="row">
    <svg width="16" height="16" viewBox="0 0 24 24"><path fill="#ddd" d="M6.6 10.8a15.1 15.1 0 0 0 6.6 6.6l2.2-2.2c.3-.3.7-.4 1-.2 1.1.4 2.3.6 3.6.6.6 0 1 .4 1 1V20c0 .6-.4 1-1 1A17 17 0 0 1 3 4c0-.6.4-1 1-1h3.5c.6 0 1 .4 1 1 0 1.3.2 2.5.6 3.6.1.3 0 .7-.2 1z"/></svg>
    Call Us 555.218.3904
  </div>
  <div class="row">
    <svg width="18" height="14" viewBox="0 0 18 14" fill="none" stroke="#ddd" stroke-width="1.4"><rect x="1" y="1" width="16" height="12"/><path d="M1 1l8 7 8-7"/></svg>
    Email: info@varrowickbr.org
  </div>
</div>

<div class="links footer-col abs">
  <h3>QUICK LINKS</h3>
  <ul><li>Home</li><li>About us</li><li>Services</li><li>Resources</li><li>FAQ</li><li>Contact Us</li></ul>
</div>

<div class="footer-bar abs">2017 © Copyrights Varrowick Biomedical Research Institute.All Rights Reserved</div>

</body>
</html>
```